IronPeak 317

Brochure must include all info on the mock up of the brochure I have put together in Word. A similar design would be great but a little more professional would be great.

Industry/Entity Type

It Professional

Requirements
Must have
• MUST INCLUDE ALL INFORMATION IN MOCK UP

```html
<!DOCTYPE html>
<html lang="en">
<head>
<meta charset="UTF-8">
<title>IronPeak 317 – On Ramp &amp; Memberships</title>
<link rel="stylesheet" href="https://fonts.googleapis.com/css2?family=Oswald:wght@600;700&family=Roboto+Condensed:wght@400;500;700&display=swap">
<style>
  :root {
    --gold: #f5c300;
    --white: #ffffff;
    --ink: #111111;
    --bg-dark: #141414;
    --bg-mid: #3a3a3a;
    --display: "Oswald", "Arial Narrow", sans-serif;
    --body: "Roboto Condensed", "Arial Narrow", sans-serif;
  }
  html, body { margin: 0; padding: 0; overflow: hidden; background: var(--bg-dark); }
  .brochure {
    position: relative;
    width: 1200px;
    height: 927px;
    overflow: hidden;
    font-family: var(--body);
    color: var(--white);
  }
  .backdrop {
    position: absolute; inset: 0;
    background:
      radial-gradient(ellipse 38% 55% at 50% 38%, rgba(120,120,120,.55), rgba(0,0,0,0) 70%),
      radial-gradient(ellipse 30% 40% at 80% 20%, rgba(90,90,90,.35), rgba(0,0,0,0) 70%),
      linear-gradient(180deg, var(--bg-mid) 0%, #202020 55%, var(--bg-dark) 100%);
  }
  .column { position: absolute; top: 68px; text-align: center; }
  .column--intro { left: 27px; width: 370px; }
  .column--signup { left: 413px; width: 380px; }
  .column--memberships { left: 800px; width: 376px; }
  .title {
    margin: 0;
    font-family: var(--display);
    font-weight: 700;
    font-size: 51px;
    line-height: 45px;
    color: var(--gold);
    text-transform: uppercase;
    letter-spacing: .5px;
  }
  .column--intro .title { width: 370px; }
  .subtitle {
    margin: 7px 0 0;
    font-family: var(--body);
    font-weight: 700;
    font-size: 33px;
    line-height: 36px;
    white-space: nowrap;
  }
  .intro-text {
    margin: 25px 0 0;
    text-align: left;
    font-size: 16.3px;
    line-height: 22.8px;
    font-weight: 500;
    white-space: nowrap;
  }
  .steps { list-style: none; margin: 0; padding: 0; }
  .step {
    position: absolute; left: 0; width: 100%;
    font-size: 16.3px; line-height: 23px; font-weight: 500;
    white-space: nowrap;
  }
  .step__label {
    display: block;
    font-weight: 700;
    font-size: 20px;
    line-height: 26px;
    color: var(--gold);
    margin-bottom: 1px;
  }
  .step--1 { top: 164px; } .step--2 { top: 254px; } .step--3 { top: 346px; }
  .step--4 { top: 457px; } .step--5 { top: 548px; } .step--6 { top: 661px; }
  .tiers { list-style: none; margin: 0; padding: 0; }
  .tier {
    position: absolute; left: 0; width: 100%;
    font-size: 16.3px; line-height: 23px; font-weight: 500;
    white-space: nowrap;
  }
  .tier__name { display: block; font-weight: 700; font-size: 20px; color: var(--gold); line-height: 26px; }
  .tier--1 { top: 119px; } .tier--2 { top: 189px; } .tier--3 { top: 258px; }
  .tier--4 { top: 349px; } .tier--5 { top: 416px; } .tier--6 { top: 487px; }
  .tier--7 { top: 558px; } .tier--8 { top: 625px; } .tier--9 { top: 695px; }
  .contact-bar {
    position: absolute;
    left: 27px; top: 830px;
    width: 1146px; height: 68px;
    background: var(--gold);
    color: var(--ink);
    text-align: center;
    font-weight: 700;
    font-size: 19px;
    line-height: 26px;
    padding-top: 8px;
    box-sizing: border-box;
    white-space: nowrap;
  }
  .contact-bar p { margin: 0; }
  .contact-bar .sep { margin: 0 30px; }
</style>
</head>
<body>
<main class="brochure">
  <div class="backdrop" role="img" aria-label="Dark gritty photograph of an athlete training in the gym"></div>

  <section class="column column--intro">
    <h2 class="title">Our<br>“On Ramp”<br>Program</h2>
    <p class="intro-text">The emphasis in the On-Ramp program is on skill<br>development and exposure to our basic move-<br>ments. It is designed to prepare beginners, or<br>those who have not done IronPeak before, to enter<br>our ongoing group classes. In the program we<br>be hammering technique— both to ensure your<br>safety—and success at the next level.” &nbsp;It is a<br>program that involves 8 sessions. In these<br>sessions we will introduce you to technique and<br>mechanics first, then intensity. We will explain<br>how to understand our daily WOD (Workout Of<br>the Day) which is written up on our whiteboard<br>and found on our website. We will be showing<br>you movements that begin with the relatively<br>non technical movements and then move on to<br>progressively more technical. &nbsp;There will be a<br>workout at the end of each session which will<br>get progressively more challenging as the course<br>progresses. The difficulty of these workouts is<br>ultimately in your hands…the degree that you<br>push yourself will determine how much<br>suffering goes on. &nbsp;The class is called “On Ramp”<br>for a specific reason…we want to ramp you up to<br>the level of intensity and output that is inherent in<br>our group .</p>
  </section>

  <section class="column column--signup">
    <h2 class="title">How Do I<br>Sign Up</h2>
    <p class="subtitle">A Step by Step Guide</p>
    <ol class="steps">
      <li class="step step--1"><span class="step__label">STEP 1</span>The first step is to go to our home page at<br>www.ironpeak317.com</li>
      <li class="step step--2"><span class="step__label">STEP 2</span>Under the “Membership” tab click on<br>“Sign Up”</li>
      <li class="step step--3"><span class="step__label">STEP 3</span>Select “On-Ramp Program” or if you have IronPeak<br>experience you can select one of our other<br>memberships</li>
      <li class="step step--4"><span class="step__label">STEP 4</span>Once you have entered your email address you<br>will be sent a password</li>
      <li class="step step--5"><span class="step__label">STEP 5</span>Once that is done you can go into your account<br>and enter your payment details or pay the next<br>time you are in.</li>
      <li class="step step--6"><span class="step__label">STEP 6</span>Using your email address and password you can<br>now book into the classes you wish to attend.</li>
    </ol>
  </section>

  <section class="column column--memberships">
    <h2 class="title">Memberships</h2>
    <p class="subtitle">Types &amp; Prices</p>
    <ul class="tiers">
      <li class="tier tier--1"><span class="tier__name">Monthly Unlimited</span>$200 &nbsp;(Unlimited classes for a month)</li>
      <li class="tier tier--2"><span class="tier__name">Monthly (3 Days Per Week)</span>$155 &nbsp;(3 classes per week)</li>
      <li class="tier tier--3"><span class="tier__name">On-Ramp Beginners Program</span>$100 / 8 classes- 1 Month Limit<br>(one time only offer)</li>
      <li class="tier tier--4"><span class="tier__name">Transition Program</span>$130 &nbsp;(8 Sessions - 1 Month limit)</li>
      <li class="tier tier--5"><span class="tier__name">20-Class Pass</span>$370 / 20 classes ($18.50/class)</li>
      <li class="tier tier--6"><span class="tier__name">10 Class Pass</span>$200 / 10 classes ($20/class)</li>
      <li class="tier tier--7"><span class="tier__name">Drop-In</span>$25 &nbsp;(Must Have IronPeak Experience)</li>
      <li class="tier tier--8"><span class="tier__name">12 Month Unlimited</span>$1,800 &nbsp;Unlimited Membership (Unlimited classes)</li>
      <li class="tier tier--9"><span class="tier__name">6 Month Unlimited</span>$1,000 &nbsp;Unlimited Membership (Unlimited classes)</li>
    </ul>
  </section>

  <footer class="contact-bar">
    <p>CONTACT US AT</p>
    <p>Website: ironpeak317.com<span class="sep">/</span>Email: administration@ironpeak317.com<span class="sep">/</span>Ph: 9044-3186</p>
  </footer>
</main>
</body>
</html>
```